Web Button design and production

I need remote control like buttons (or your own design of buttons if I like it)
3x4 text buttons (normal, pressed, disabled)
3x1 empty button (normal, pressed, disabled)
3x6 buttons with glyph (normal, pressed, disabled)
3x288 with 24h time "00:00", "00:05", "00:10" (normal, pressed, disabled)
4 LED (red, green, orange, black)
I will upload the background image as soon as possible (black plastic)
See attached images
Q: Do the buttons have to be gray/black?
A: It should look like a high end remote control. It could be brushed aluminum as well, or something you come up with. But I guess black or dark grey would be best. The background will be pixelvaultimages 40631758, but it's not available yet.
Q: Do I have to provide all buttons for the contest?
A: No! I only need one button (3 states) and a LED to decide. Only the winner will do the whole job.
Q: Is the Designer who wins the contest expected to complete all the extra buttons?
A: Yes, please.
Plastic

```html
<!DOCTYPE html>
<html lang="en">
<head>
<meta charset="utf-8">
<title>Remote Control Buttons</title>
<link rel="stylesheet" href="https://fonts.googleapis.com/css2?family=Open+Sans:wght@600;700&display=swap">
<style>
  :root {
    --bg-center: #2b313b;
    --bg-edge: #16191e;
    --well: #1c2027;
    --well-edge: #12151a;
    --metal-light: #f4f4f4;
    --metal-mid: #c9c9c9;
    --metal-dark: #9a9a9a;
    --ink: #2a2c30;
    --ink-faded: #b8b8b8;
    --green-light: #b8f24a;
    --green: #8ad61c;
    --green-dark: #5e9e0c;
    --led-red: #c0181a;
    --led-green: #a6ff1e;
    --led-off: #2e3238;
  }
  * { margin: 0; padding: 0; box-sizing: border-box; }
  html, body { width: 1200px; height: 900px; overflow: hidden; }
  body {
    background: radial-gradient(ellipse 700px 600px at 600px 420px, var(--bg-center), var(--bg-edge));
    font-family: "Open Sans", Arial, sans-serif;
    position: relative;
  }
  .control { position: absolute; width: 124px; height: 124px; margin: -62px 0 0 -62px; }
  .well {
    position: absolute; inset: 0; border-radius: 50%;
    background: radial-gradient(circle at 50% 40%, #232831, var(--well));
    box-shadow: inset 0 2px 4px rgba(0,0,0,.55), 0 1px 0 rgba(255,255,255,.05);
  }
  .knob {
    position: absolute; left: 16px; top: 16px; width: 92px; height: 92px; border-radius: 50%;
    background:
      radial-gradient(circle, rgba(255,255,255,.35), rgba(255,255,255,0) 70%),
      conic-gradient(from 10deg, var(--metal-light), var(--metal-dark) 12%, var(--metal-light) 25%, var(--metal-mid) 37%, var(--metal-light) 50%, var(--metal-dark) 62%, var(--metal-light) 75%, var(--metal-mid) 87%, var(--metal-light));
    box-shadow: inset 0 1px 1px rgba(255,255,255,.9), inset 0 -1px 2px rgba(0,0,0,.25), 0 2px 3px rgba(0,0,0,.5);
    display: flex; align-items: center; justify-content: center;
    color: var(--ink);
  }
  .control.is-raised .knob {
    box-shadow: inset 0 1px 1px rgba(255,255,255,.9), 0 6px 10px rgba(0,0,0,.55), 0 20px 26px rgba(0,0,0,.45);
  }
  .control.is-disabled .knob { color: var(--ink-faded); }
  .glyph { width: 34px; height: 26px; }
  .control.is-disabled .glyph path { fill: none; stroke: #8c8c8c; stroke-width: 1.2; }
  .time { font-weight: 700; font-size: 27px; line-height: 22px; text-align: center; letter-spacing: -0.5px; }
  .time .sep { display: block; font-size: 14px; line-height: 8px; }
  .control.is-disabled .time { font-weight: 600; color: #d8d8d8; -webkit-text-stroke: 0.8px #8a8a8a; }
  .knob.is-lamp {
    background: conic-gradient(var(--metal-light), var(--metal-dark) 25%, var(--metal-light) 50%, var(--metal-dark) 75%, var(--metal-light));
  }
  .lamp { width: 74px; height: 74px; border-radius: 50%; }
  .lamp.is-off { background: radial-gradient(circle at 50% 35%, #ffffff, #dedfe0 70%, #c8c9ca); box-shadow: inset 0 1px 2px rgba(0,0,0,.3); }
  .lamp.is-on { background: radial-gradient(circle at 50% 30%, var(--green-light), var(--green) 60%, var(--green-dark)); box-shadow: inset 0 1px 2px rgba(0,0,0,.3); }
  .led { position: absolute; width: 34px; height: 9px; margin-left: -17px; border-radius: 3px; }
  .led.red { background: var(--led-red); box-shadow: 0 0 3px rgba(255,40,40,.6), inset 0 1px 1px rgba(255,120,120,.5); }
  .led.green { background: var(--led-green); box-shadow: 0 0 6px rgba(166,255,30,.8), inset 0 1px 1px rgba(240,255,200,.7); }
  .led.off { background: repeating-linear-gradient(45deg, var(--led-off) 0 2px, #24282d 2px 4px); box-shadow: inset 0 1px 1px rgba(0,0,0,.6); }
</style>
</head>
<body>
  <svg width="0" height="0" style="position:absolute">
    <defs>
      <path id="ff" d="M2 2 L16 13 L2 24 Z M17 2 L31 13 L17 24 Z"/>
    </defs>
  </svg>

  <!-- glyph row -->
  <div class="control is-disabled" style="left:433px;top:172px"><div class="well"></div><div class="knob"><svg class="glyph" viewBox="0 0 34 26"><path d="M2 2 L16 13 L2 24 Z M17 2 L31 13 L17 24 Z"/></svg></div></div>
  <div class="control is-raised" style="left:586px;top:172px"><div class="well"></div><div class="knob"><svg class="glyph" viewBox="0 0 34 26"><use href="#ff" fill="#2a2c30"/></svg></div></div>
  <div class="control" style="left:736px;top:172px"><div class="well"></div><div class="knob"><svg class="glyph" viewBox="0 0 34 26"><use href="#ff" fill="#3a3c40"/></svg></div></div>
  <div class="led red" style="left:433px;top:259px"></div>
  <div class="led off" style="left:586px;top:259px"></div>
  <div class="led green" style="left:736px;top:259px"></div>

  <!-- time row -->
  <div class="control is-disabled" style="left:433px;top:440px"><div class="well"></div><div class="knob"><div class="time">00<span class="sep">⁚</span>05</div></div></div>
  <div class="control is-raised" style="left:586px;top:440px"><div class="well"></div><div class="knob"><div class="time">00<span class="sep">⁚</span>05</div></div></div>
  <div class="control" style="left:736px;top:440px"><div class="well"></div><div class="knob"><div class="time">00<span class="sep">⁚</span>05</div></div></div>
  <div class="led red" style="left:433px;top:528px"></div>
  <div class="led off" style="left:586px;top:528px"></div>
  <div class="led green" style="left:736px;top:528px"></div>

  <!-- empty lamp row -->
  <div class="control is-disabled" style="left:433px;top:698px"><div class="well"></div><div class="knob is-lamp"><div class="lamp is-off"></div></div></div>
  <div class="control is-raised" style="left:586px;top:698px"><div class="well"></div><div class="knob is-lamp"><div class="lamp is-on"></div></div></div>
  <div class="control" style="left:736px;top:698px"><div class="well"></div><div class="knob is-lamp"><div class="lamp is-on"></div></div></div>
  <div class="led red" style="left:433px;top:788px"></div>
  <div class="led off" style="left:586px;top:788px"></div>
  <div class="led green" style="left:736px;top:788px"></div>
</body>
</html>
```